Financial Advisor Brochure to attract new clients

I am launching a new career as a Financial Advisor and a flier that shows what services I offer and why I decided to go back to work at this point in my life. I have a deep desire to help people meet their dreams and believe that a solid financial foundation provides the ability to live your life as you want to and not how you have to. I created a simple flier but know that so much more can be done to catch a persons eye.

Target Market(s)

Entrepeneurs and Woman in all stages of life.

Industry/Entity Type

Financial Advisor

Font styles to use
Sans Serif

Colors
00AB8E
00BBA5
67D7C9
C6EFE9
E9F9F6

Requirements
Must have
• my photo, contact information and Tessaly Logo

```html
<!DOCTYPE html>
<html lang="en">
<head>
<meta charset="utf-8">
<title>Marla Keswick – Financial Advisor Flyer</title>
<link href="https://fonts.googleapis.com/css2?family=Open+Sans:wght@400;600&family=Merriweather:wght@400&display=swap" rel="stylesheet">
<style>
  :root {
    --sky: #4fc6e8;
    --sky-deep: #2fb0da;
    --navy: #1f4c98;
    --ink: #1d3f7f;
    --white: #ffffff;
    --backdrop: #eceef0;
  }
  * { box-sizing: border-box; margin: 0; padding: 0; }
  html, body { width: 1200px; height: 960px; overflow: hidden; background: var(--backdrop); }
  .flyer {
    position: absolute; left: 280px; top: 60px; width: 640px; height: 840px;
    background: var(--sky); overflow: hidden;
    box-shadow: 0 10px 30px rgba(0,0,0,.15);
  }
  .flyer__top { position: absolute; left: 0; top: 0; width: 640px; height: 400px; background: var(--white); }
  .brand { position: absolute; display: flex; align-items: center; gap: 8px;
    font-family: "Open Sans", sans-serif; font-weight: 600; color: var(--navy); }
  .brand__square { width: 14px; height: 14px; background: var(--navy); }
  .brand--top { left: 36px; top: 30px; font-size: 20px; }
  .brand--bottom { right: 30px; bottom: 28px; font-size: 24px; color: var(--white); }
  .brand--bottom .brand__square { background: var(--navy); width: 20px; height: 20px; }
  .portrait {
    position: absolute; left: 340px; top: 24px; width: 300px; height: 376px;
    background: linear-gradient(170deg, #f3f8fb 0%, #8fd3ee 45%, #3ab6e0 100%);
  }
  .advisor { position: absolute; left: 36px; top: 92px; width: 300px; }
  .advisor__name { font-family: "Open Sans", sans-serif; font-weight: 600; font-size: 27px;
    color: var(--sky-deep); letter-spacing: .5px; line-height: 1.1; }
  .advisor__title { font-family: "Merriweather", serif; font-size: 17px; color: var(--ink); margin-top: 2px; }
  .tag { display: inline-block; background: var(--sky); color: var(--white);
    font-family: "Open Sans", sans-serif; font-size: 12px; padding: 2px 6px; letter-spacing: .3px; }
  .profile { margin-top: 10px; }
  .profile__text { border: 1px solid var(--ink); padding: 8px 10px; margin-top: -1px;
    font-family: "Merriweather", serif; font-size: 11.5px; line-height: 1.45; color: var(--ink); }
  .cta { margin-top: 14px; }
  .cta .tag { font-size: 13px; padding: 4px 10px; }
  .contacts { list-style: none; margin-top: 12px; }
  .contacts li { display: flex; align-items: center; gap: 9px; margin-bottom: 6px;
    font-family: "Merriweather", serif; font-size: 11.5px; color: var(--ink); }
  .contacts svg { width: 13px; height: 13px; flex: none; }
  .band { position: absolute; left: 0; top: 400px; width: 640px; height: 22px; background: var(--navy); }
  .services__heading { position: absolute; left: 0; top: 432px; width: 640px; text-align: center;
    font-family: "Open Sans", sans-serif; font-size: 17px; color: var(--white); letter-spacing: .6px; }
  .services { position: absolute; left: 40px; top: 470px; width: 560px; }
  .service { margin-bottom: 7px; }
  .service .tag { background: var(--navy); font-size: 10.5px; padding: 1px 6px; }
  .service ul { list-style: none; margin-top: 2px; }
  .service li { font-family: "Merriweather", serif; font-size: 10.5px; line-height: 1.55;
    color: var(--ink); text-transform: uppercase; padding-left: 14px; position: relative; }
  .service li::before { content: ""; position: absolute; left: 3px; top: 7px; width: 4px; height: 4px;
    border-radius: 50%; background: var(--ink); }
</style>
</head>
<body>
<main class="flyer">
  <section class="flyer__top">
    <div class="brand brand--top"><span class="brand__square"></span>Tessaly</div>
    <div class="portrait" role="img" aria-label="Portrait photo of the advisor with a blue 3D growth chart illustration"></div>
    <div class="advisor">
      <h1 class="advisor__name">MARLA KESWICK</h1>
      <p class="advisor__title">Financial Advisor</p>
      <div class="profile">
        <span class="tag">PROFILE</span>
        <p class="profile__text">Passionate about helping empower you with knowledge to make informed financial decisions throughout all of life's stages and help you achieve your goals.</p>
      </div>
      <div class="cta"><span class="tag">CALL FOR AN APPOINTMENT</span></div>
      <ul class="contacts">
        <li><svg viewBox="0 0 24 24"><path fill="#2fb0da" d="M6.6 10.8a15 15 0 0 0 6.6 6.6l2.2-2.2c.3-.3.7-.4 1-.2 1.1.4 2.3.6 3.6.6.6 0 1 .4 1 1V20c0 .6-.4 1-1 1A17 17 0 0 1 3 4c0-.6.4-1 1-1h3.5c.6 0 1 .4 1 1 0 1.3.2 2.5.6 3.6.1.3 0 .7-.2 1z"/></svg>407-555-0182</li>
        <li><svg viewBox="0 0 24 24"><rect x="2" y="5" width="20" height="14" fill="#2fb0da"/><path d="M2 5l10 8 10-8" fill="none" stroke="#fff" stroke-width="1.6"/></svg>marla.keswick@tessalywealthalliance.com</li>
        <li><svg viewBox="0 0 24 24"><circle cx="12" cy="12" r="10" fill="#2fb0da"/><path d="M2 12h20M12 2c3 3 3 17 0 20M12 2c-3 3-3 17 0 20" fill="none" stroke="#fff" stroke-width="1.3"/></svg>www.tessalywealthalliance.com</li>
      </ul>
    </div>
  </section>
  <div class="band"></div>
  <h2 class="services__heading">FINANCIAL PLANNING SERVICES OFFERED</h2>
  <section class="services">
    <div class="service"><span class="tag">TRANSITION PLANNING</span>
      <ul><li>Divorce planning.</li><li>Strategy and guidance pre, during, and post- divorce</li></ul></div>
    <div class="service"><span class="tag">RETIREMENT PLANNING</span>
      <ul><li>Current portfolio analysis</li><li>Timeline asset and income planning</li><li>Tax and estate review and projections</li></ul></div>
    <div class="service"><span class="tag">REAL ESTATE ACQUISITION OR SALE</span>
      <ul><li>Acquisition or dissolution of real estate. Individual or portfolio</li></ul></div>
    <div class="service"><span class="tag">BUSINESS SALE OR PURCHASE</span>
      <ul><li>Company valuations</li><li>Tax impact analysis</li><li>Strategy implementation for funds received from sale.</li></ul></div>
    <div class="service"><span class="tag">ESTATE PLANNING</span>
      <ul><li>Strategies for creating future generational wealth.</li></ul></div>
    <div class="service"><span class="tag">NEW INVESTORS</span>
      <ul><li>Assistance in opening investment and retirement accounts</li></ul></div>
  </section>
  <div class="brand brand--bottom"><span class="brand__square"></span>Tessaly</div>
</main>
</body>
</html>
```